Property Investment Brouchure Design

I would like a brochure designed to present property investment opportunities. The brochure will showcase one property or a portfolio of properties at one time. The brochure will need to be designed as a template which will need to be able to be editable via power point or an Mac program.

The brochure will need to be 12 pages in length and entail the following information:

1) Cover page
This page will include a full page high res image of the property with a catch phrase and the words confidential. Again the title will be in off white over the top of a charcoal transparent box.

2) Executive Summary
This page will include a small bit of information for each of the categories listed below over the top of a full page image. Again the content will be in off white over the top of a charcoal transparent box

3) Investment highlights
This page will include a small bit of information at the bottom of the page over the top of a full page high res image. Again the content will be in off white over the top of a charcoal transparent box.

4) Property Location
This page will include a full page areal images marked location of the property with close by amenities also marked out. This will need to be changed for each new document. This locations should be marked out with a tranpernt box in a light blue or charcoal colour.

5) Tenancy page
This page will include a full page image of the tenants business premise, a logo for the tenant at the top of the page and information about the tenant in the middle of the page with lease information for each tenant in a table template listed at the bottom of the page. This same page will be used a number of times for properties that have multiple tenants.

6) Financial information
This page will include the following information
* various income streams in the form of a pie graph showing a percent for each stream
* various outgoing streams in the form of a pie graph showing a percent for each stream
* line graph showing the difference between the income and outgoings
* line graph showing vacancy rates over the year
* pie graph showing the different market share for customers who stay at the property, this will also include a percentage for each group
* bar graph showing the lease expires for each tenant

7) Town Planning Information
This page will include a full page ariel image showing the location of the property then a zoning map will be overlayed showing the current property zoning and information will appear on the side of the map outlining the current planning controls. From here another map will be overlayed showing the new draft zoning map and information will appear outlining the new draft planning controls.

8) Opportunity scope
This page will include a full page image showing the current property then an image of the improvement opportunity that is within the property investment (image of current property then an artist impression of what can be built if the property is a development site, current floor plans and then new floor plans if the opportunity is an internal opportunity etc)
There will be information outlining the opportunity on the side of the page
There will be a line graph at the bottom of the page showing the current income and the potential new income

9) Market update
this page will include a full page image of the city CBD with information on the hotel market floating over top. This information will also include a pie graph showing the market share of all the large companies in the market. This information will be updated every quarter. This page will also includeq information on Forgeion investment.

10) Services offered
This page will include another full page image will information about other services we have contacts in. (e.g: asset management, financial, etc)

11) Conclusion / Contact Details / Disclaimer
This page will include information on the conclusion of the property including contact details our company logo and small print at the bottom of the page outlining the disclaimer information.

12) Back Page
This page will just have a full page image of the investment

The type of designed required will include:

- There must be full page high resolution images on each page
- Graph icons (pie, line and bar graphs) showcasing the financial information on the financial page
- Professional but very simple
- all content must be displayed over the top of a transparent box. The writing show be in a off white color and the box show be in a transparent charcoal colour
- The design will need to be able to be edited in Power point or a mac program once the template has been completed
- The design will also need to be user friendly via email / PDF
- the file must be able to be presented via an iPad

Target Market(s)

High net worth individuals

Industry/Entity Type

Investment

Requirements
Must have
• Simple Design
Full size high res images on every page
All content must be floating over the top of a transparent box. The text should be in a off white color and the box should be in a transparent charcoal colour (please see the attachments and the QD website for examples)
Pie,line and bar graph on the financial page
Professional / Creative Text Font (please see the QD website)
Template design which the images and content will be able to be changed via PowerPoint or a Mac program for other properties
Only use two colors throughout (ie: just off white and charcoal for the content and box, and a different shade of the two for the graphs, everything else will just be high res images)
Must be able to be presented via an iPad, be sent via email and be printed if need be
Should not have
• Standard Text
Boarders
No harsh white of dark black background
Too many small photos
Too much information on one page
Too many different colours

```html
<!DOCTYPE html>
<html lang="en">
<head>
<meta charset="utf-8">
<title>Financial Information – Brochure Pages</title>
<link rel="stylesheet" href="https://fonts.googleapis.com/css2?family=Oswald:wght@300;400&family=Cormorant+Garamond:ital,wght@1,500&display=swap">
<style>
  :root {
    --backdrop: #ececea;
    --charcoal-glass: rgba(38, 38, 42, 0.78);
    --off-white: #f2efe8;
    --graph-grey: #b8bcc6;
    --graph-grey-dark: #9ea3ae;
    --graph-orange: #f0a01e;
    --graph-gold: #f8c51c;
    --photo-sky: #5a6f95;
    --photo-trees: #23281f;
    --photo-house: #3a3630;
    --photo-lawn: #2f3a22;
    --photo-stone: #5b5752;
  }
  * { box-sizing: border-box; margin: 0; padding: 0; }
  html, body { width: 1200px; height: 728px; overflow: hidden; background: var(--backdrop); }
  .canvas { position: relative; width: 1200px; height: 728px; }

  .page { position: absolute; overflow: hidden; }
  .page--income { left: 31px; top: 20px; width: 590px; height: 445px; }
  .page--vacancy { left: 562px; top: 244px; width: 592px; height: 442px; }

  .page__photo {
    position: absolute; inset: 0;
    background:
      radial-gradient(ellipse 60% 18% at 50% 48%, rgba(214, 140, 60, 0.35), transparent 70%),
      linear-gradient(180deg, var(--photo-sky) 0%, var(--photo-trees) 16%, var(--photo-house) 42%, var(--photo-trees) 55%, var(--photo-lawn) 72%, var(--photo-stone) 100%);
  }

  .glass { position: absolute; background: var(--charcoal-glass); }

  .heading {
    position: absolute; color: var(--off-white);
    font-family: "Oswald", sans-serif; font-weight: 300;
    text-transform: uppercase; letter-spacing: 0.14em; line-height: 1.15;
  }
  .heading--chart { font-size: 16px; transform: translateX(-50%); white-space: nowrap; }
  .heading--side { font-size: 16px; }
  .heading--title { font-size: 25px; font-weight: 400; letter-spacing: 0.16em; text-align: center; transform: translateX(-50%); white-space: nowrap; line-height: 1.2; }

  .label {
    position: absolute; color: var(--off-white);
    font-family: "Cormorant Garamond", serif; font-style: italic; font-weight: 500;
    font-size: 8px; white-space: nowrap;
  }
  .graph { position: absolute; overflow: visible; }
</style>
</head>
<body>
<main class="canvas">

  <!-- Page: income and outgoings -->
  <section class="page page--income">
    <div class="page__photo" role="img" aria-label="Full-page photograph of the investment property at dusk, a timber house with lit windows and a stone path across the lawn"></div>

    <div class="glass" style="left:30px;top:31px;width:257px;height:270px;"></div>
    <div class="glass" style="left:304px;top:31px;width:259px;height:270px;"></div>
    <div class="glass" style="left:30px;top:315px;width:257px;height:100px;"></div>

    <h2 class="heading heading--chart" style="left:158px;top:46px;">Income Streams</h2>
    <svg class="graph" style="left:60px;top:70px;" width="200" height="100" viewBox="0 0 200 100">
      <circle cx="94" cy="48" r="37" fill="none" stroke="var(--graph-grey)" stroke-width="8"/>
      <circle cx="94" cy="48" r="37" fill="none" stroke="var(--graph-orange)" stroke-width="8" stroke-dasharray="88 145" transform="rotate(-75 94 48)"/>
      <g stroke="var(--off-white)" stroke-width="0.8" fill="var(--off-white)">
        <line x1="0" y1="24" x2="82" y2="24"/><circle cx="82" cy="24" r="1.4"/>
        <line x1="0" y1="88" x2="58" y2="88"/><circle cx="58" cy="88" r="1.4"/>
        <line x1="127" y1="52" x2="148" y2="52"/><circle cx="127" cy="52" r="1.4"/>
        <line x1="120" y1="84" x2="148" y2="84"/><circle cx="120" cy="84" r="1.4"/>
      </g>
    </svg>
    <span class="label" style="left:63px;top:84px;">stream one</span>
    <span class="label" style="left:63px;top:148px;">stream two</span>
    <span class="label" style="left:216px;top:116px;">stream three</span>
    <span class="label" style="left:216px;top:148px;">stream four</span>

    <h2 class="heading heading--chart" style="left:432px;top:46px;">Outgoing&nbsp;&nbsp;Streams</h2>
    <svg class="graph" style="left:333px;top:70px;" width="200" height="100" viewBox="0 0 200 100">
      <circle cx="94" cy="48" r="37" fill="none" stroke="var(--graph-grey)" stroke-width="8"/>
      <circle cx="94" cy="48" r="37" fill="none" stroke="var(--graph-orange)" stroke-width="8" stroke-dasharray="82 151" transform="rotate(-62 94 48)"/>
      <g stroke="var(--off-white)" stroke-width="0.8" fill="var(--off-white)">
        <line x1="0" y1="24" x2="82" y2="24"/><circle cx="82" cy="24" r="1.4"/>
        <line x1="0" y1="88" x2="58" y2="88"/><circle cx="58" cy="88" r="1.4"/>
        <line x1="127" y1="52" x2="148" y2="52"/><circle cx="127" cy="52" r="1.4"/>
        <line x1="120" y1="84" x2="148" y2="84"/><circle cx="120" cy="84" r="1.4"/>
      </g>
    </svg>
    <span class="label" style="left:336px;top:84px;">stream one</span>
    <span class="label" style="left:336px;top:148px;">stream two</span>
    <span class="label" style="left:489px;top:116px;">stream three</span>
    <span class="label" style="left:489px;top:148px;">stream four</span>

    <h2 class="heading heading--side" style="left:56px;top:233px;">Income vs<br>Outgoings</h2>
    <svg class="graph" style="left:160px;top:213px;" width="268" height="86" viewBox="0 0 300 96">
      <polygon fill="var(--graph-grey)" points="0,96 14,84 24,72 34,78 46,50 56,66 66,40 78,58 90,30 100,52 112,22 122,44 134,28 146,6 152,34 162,18 170,42 182,26 192,50 204,36 214,60 228,48 240,70 254,62 270,82 284,78 300,96"/>
      <polygon fill="var(--graph-orange)" points="20,96 40,80 56,84 70,62 84,74 96,48 108,66 120,40 132,58 144,30 156,54 168,38 180,62 194,50 206,72 222,66 238,84 256,82 274,92 280,96"/>
      <line x1="146" y1="6" x2="146" y2="96" stroke="var(--off-white)" stroke-width="0.8"/>
      <polyline fill="none" stroke="var(--graph-gold)" stroke-width="1" points="4,92 40,84 70,72 96,60 120,52 146,40 170,52 194,62 222,74 256,86 296,92"/>
      <g fill="var(--off-white)"><circle cx="70" cy="72" r="1.6"/><circle cx="120" cy="52" r="1.6"/><circle cx="146" cy="6" r="2"/><circle cx="194" cy="62" r="1.6"/><circle cx="256" cy="86" r="1.6"/></g>
    </svg>

    <h1 class="heading heading--title" style="left:158px;top:342px;">Financial<br>Information</h1>
  </section>

  <!-- Page: vacancy, stays and lease expiry -->
  <section class="page page--vacancy">
    <div class="page__photo" role="img" aria-label="Full-page photograph of the investment property at dusk, a timber house with lit windows and a stone path across the lawn"></div>

    <div class="glass" style="left:30px;top:30px;width:532px;height:98px;"></div>
    <div class="glass" style="left:30px;top:141px;width:257px;height:162px;"></div>
    <div class="glass" style="left:304px;top:141px;width:258px;height:162px;"></div>
    <div class="glass" style="left:30px;top:315px;width:257px;height:100px;"></div>

    <h2 class="heading heading--side" style="left:63px;top:62px;">Vacancy<br>Rate</h2>
    <svg class="graph" style="left:162px;top:37px;" width="295" height="86" viewBox="0 0 300 96">
      <polygon fill="var(--graph-grey)" points="0,96 14,84 24,72 34,78 46,50 56,66 66,40 78,58 90,30 100,52 112,22 122,44 134,28 146,6 152,34 162,18 170,42 182,26 192,50 204,36 214,60 228,48 240,70 254,62 270,82 284,78 300,96"/>
      <polygon fill="var(--graph-orange)" points="20,96 40,80 56,84 70,62 84,74 96,48 108,66 120,40 132,58 144,30 156,54 168,38 180,62 194,50 206,72 222,66 238,84 256,82 274,92 280,96"/>
      <line x1="146" y1="6" x2="146" y2="96" stroke="var(--off-white)" stroke-width="0.8"/>
      <polyline fill="none" stroke="var(--graph-gold)" stroke-width="1" points="4,92 40,84 70,72 96,60 120,52 146,40 170,52 194,62 222,74 256,86 296,92"/>
      <g fill="var(--off-white)"><circle cx="70" cy="72" r="1.6"/><circle cx="120" cy="52" r="1.6"/><circle cx="146" cy="6" r="2"/><circle cx="194" cy="62" r="1.6"/><circle cx="256" cy="86" r="1.6"/></g>
    </svg>

    <h2 class="heading heading--chart" style="left:158px;top:157px;">Customers Who Stay</h2>
    <svg class="graph" style="left:63px;top:185px;" width="200" height="100" viewBox="0 0 200 100">
      <circle cx="94" cy="48" r="37" fill="none" stroke="var(--graph-grey)" stroke-width="8"/>
      <circle cx="94" cy="48" r="37" fill="none" stroke="var(--graph-orange)" stroke-width="8" stroke-dasharray="84 149" transform="rotate(-60 94 48)"/>
      <g stroke="var(--off-white)" stroke-width="0.8" fill="var(--off-white)">
        <line x1="0" y1="16" x2="82" y2="16"/><circle cx="82" cy="16" r="1.4"/>
        <line x1="0" y1="72" x2="58" y2="72"/><circle cx="58" cy="72" r="1.4"/>
        <line x1="125" y1="36" x2="148" y2="36"/><circle cx="125" cy="36" r="1.4"/>
        <line x1="122" y1="70" x2="148" y2="70"/><circle cx="122" cy="70" r="1.4"/>
      </g>
    </svg>
    <span class="label" style="left:66px;top:191px;">stream one</span>
    <span class="label" style="left:66px;top:247px;">stream two</span>
    <span class="label" style="left:216px;top:211px;">stream three</span>
    <span class="label" style="left:216px;top:245px;">stream four</span>

    <h2 class="heading heading--chart" style="left:436px;top:157px;">Lease Expires</h2>
    <svg class="graph" style="left:330px;top:180px;" width="210" height="98" viewBox="0 0 210 98">
      <defs>
        <linearGradient id="bar-grey" x1="0" x2="1"><stop offset="0" stop-color="var(--graph-grey-dark)"/><stop offset="0.45" stop-color="var(--graph-grey)"/><stop offset="1" stop-color="var(--off-white)"/></linearGradient>
        <linearGradient id="bar-orange" x1="0" x2="1"><stop offset="0" stop-color="var(--graph-orange)"/><stop offset="1" stop-color="var(--graph-gold)"/></linearGradient>
      </defs>
      <rect x="6" y="47" width="13" height="50" fill="url(#bar-grey)"/>
      <rect x="22" y="30" width="13" height="67" fill="url(#bar-grey)" opacity="0.85"/>
      <rect x="55" y="35" width="13" height="62" fill="url(#bar-orange)"/>
      <rect x="71" y="58" width="13" height="39" fill="url(#bar-orange)"/>
      <rect x="108" y="58" width="13" height="39" fill="url(#bar-grey)"/>
      <rect x="124" y="44" width="13" height="53" fill="url(#bar-grey)" opacity="0.85"/>
      <rect x="156" y="10" width="13" height="87" fill="url(#bar-orange)"/>
      <rect x="172" y="39" width="13" height="58" fill="url(#bar-orange)"/>
    </svg>
    <span class="label" style="left:336px;top:283px;">stream one</span>
    <span class="label" style="left:384px;top:283px;">stream two</span>
    <span class="label" style="left:436px;top:283px;">stream three</span>
    <span class="label" style="left:487px;top:283px;">stream four</span>

    <h1 class="heading heading--title" style="left:158px;top:341px;">Financial<br>Information</h1>
  </section>

</main>
</body>
</html>
```